Catering Menu Package

I currently have a complete menu package, which we have redesigned as far as content, now I need to it put together in a catalog type format. It is essentially 10-12 pages in length, and will be sent for print production. Upon receiving a final edit
Updates

I have added an example gif to the project.

I did this free hand this basically what I am looking for. please change text and type to whatever you think would look best. This is a total rough design so, feel free to change any and everything. The text for the page is on the word documents. If you need more images let me know I am in the process of getting as many images uploaded for your use.

Reason: I figured we got a late jump with questions, so i am extending a few days .

Target Market(s)

The target market is business who wish to have catered luncheons, breakfasts , meetings

Industry/Entity Type

Catering

Requirements
Must have
• I have attached a copy of the text that what we want in the package, our logo, and i have also attached a catering package of another company to give you an idea what the finished product will be
Should not have
• It should not look identical to the example catering packages, these are for some inspiration we want our own design with the same type of look and feel

```html
<!DOCTYPE html>
<html lang="en">
<head>
<meta charset="utf-8">
<title>Light Breakfast Menu</title>
<link href="https://fonts.googleapis.com/css2?family=Uncial+Antiqua&family=Open+Sans:ital,wght@0,400;0,700;1,400&display=swap" rel="stylesheet">
<style>
  :root {
    --page-white: #ffffff;
    --page-cream: #fbf4b6;
    --accent-orange: #ec7418;
    --heading-green: #b7c21f;
    --frame-green: #cdd45e;
    --body-grey: #a7a59c;
    --photo-fruit: #7d8f4a;
    --photo-pink: #d9a5a8;
    --photo-cards: #e2a7c6;
    --photo-tower: #8a8a52;
    --logo-ink: #1e1e1e;
  }
  * { margin: 0; padding: 0; box-sizing: border-box; }
  html, body { width: 927px; height: 1200px; overflow: hidden; background: var(--page-white); }
  .menu-page {
    position: relative;
    width: 927px;
    height: 1200px;
    background: linear-gradient(to right, var(--page-white) 0 240px, var(--page-cream) 240px);
    font-family: "Open Sans", Verdana, sans-serif;
    overflow: hidden;
  }
  .side-rule {
    position: absolute;
    left: 237px; top: 0;
    width: 9px; height: 1200px;
    background: var(--accent-orange);
  }
  .photo {
    position: absolute;
    left: -10px;
    width: 290px;
    border: 9px solid var(--frame-green);
  }
  .photo--fruit   { top: -8px;  height: 218px; transform: rotate(-2deg); background: linear-gradient(135deg, #b3a06a, var(--photo-fruit) 55%, #55703a); }
  .photo--table   { top: 226px; height: 228px; transform: rotate(1deg);  background: linear-gradient(160deg, #f0ece6, var(--photo-pink) 60%, #b8797d); }
  .photo--cards   { top: 490px; height: 192px; transform: rotate(-4deg); background: linear-gradient(120deg, #f3d3e3, var(--photo-cards) 60%, #c97ea7); }
  .photo--tower   { top: 696px; height: 222px; transform: rotate(2deg);  background: linear-gradient(150deg, #b9a574, var(--photo-tower) 55%, #4f6b33); }

  .brand {
    position: absolute;
    left: 48px; top: 948px;
    width: 150px;
    text-align: center;
    color: var(--logo-ink);
    font-family: "Open Sans", Verdana, sans-serif;
    font-weight: 700;
    font-size: 21px;
    line-height: 1.2;
  }
  .brand-mark {
    display: block;
    width: 96px; height: 96px;
    margin: 0 auto 22px;
    background: var(--accent-orange);
  }

  .menu-title {
    position: absolute;
    left: 246px; right: 0; top: 52px;
    text-align: center;
    font-family: "Uncial Antiqua", serif;
    font-size: 31px;
    letter-spacing: 2px;
    color: var(--accent-orange);
    font-weight: 400;
  }
  .menu-item { position: absolute; left: 310px; width: 560px; }
  .menu-item h2 {
    text-align: center;
    color: var(--heading-green);
    font-size: 24px;
    font-weight: 700;
    letter-spacing: 0.5px;
    margin-bottom: 14px;
    margin-right: 40px;
  }
  .menu-item p, .menu-notes p {
    color: var(--body-grey);
    font-style: italic;
    font-size: 17px;
    line-height: 26.5px;
    letter-spacing: 1.9px;
  }
  .item-quick     { top: 126px; }
  .item-farmhouse { top: 262px; }
  .item-lean      { top: 456px; }
  .item-newyorker { top: 576px; }
  .item-city      { top: 776px; }
  .menu-notes { position: absolute; left: 310px; width: 580px; top: 1074px; }
  .menu-notes p + p { margin-top: 37px; }
</style>
</head>
<body>
<main class="menu-page">
  <div class="side-rule"></div>
  <div class="photo photo--fruit" role="img" aria-label="Fruit platter display with a small white fence"></div>
  <div class="photo photo--table" role="img" aria-label="Buffet table with pink linens and pastries"></div>
  <div class="photo photo--cards" role="img" aria-label="Place cards on pink linen with starfish"></div>
  <div class="photo photo--tower" role="img" aria-label="Fruit and dip display around a tall centerpiece"></div>

  <div class="brand"><span class="brand-mark"></span>Harvest Lane Caterers</div>

  <h1 class="menu-title">Light Breakfast</h1>

  <section class="menu-item item-quick">
    <h2>Quick and Easy</h2>
    <p>French Pastry, a Fresh Baked Gourmet Muffin, and Whole Fresh Fruit (Featuring Local Apples and Peaches, California Oranges, or Bananas).</p>
  </section>
  <section class="menu-item item-farmhouse">
    <h2>Fast Farmhouse</h2>
    <p>Fresh baked Breakfast Bread and Buttery Biscuits, Whipped Butter and House-made Strawberry Jam and Local Fruit Jellies, and Whole Fresh Food (Featuring Local Apples and Peaches, California Oranges, or Bananas).</p>
  </section>
  <section class="menu-item item-lean">
    <h2>Light and Lean</h2>
    <p>Individual Yogurt, Fresh Fruit and Berry Cups and House-made Granola.</p>
  </section>
  <section class="menu-item item-newyorker">
    <h2>New Yorker</h2>
    <p>Brooklyn Bagel, Whipped Cream Cheese, House-made Strawberry Jam and Local Fruit Jellies, Whipped Butter, and Whole Fresh Fruit(Featuring Local Apples and Peaches, California Oranges, or Bananas). &nbsp;Add Smoked Salmon</p>
  </section>
  <section class="menu-item item-city">
    <h2>City Farmhouse</h2>
    <p>Fresh Baked Buttery Biscuits, Gourmet Muffins and Breakfast Breads, Brooklyn Bagels, Whole Fresh Fruit(Featuring Local Apples and Peaches, California Oranges, or Bananas), Whipped Butter and Cream Cheese, House-made Strawberry Jam and Local Fruit Jellies.</p>
  </section>

  <footer class="menu-notes">
    <p>All Prices are per Person, with a 10 person minimum order per item chosen.</p>
    <p>Local Products used when available and in season</p>
  </footer>
</main>
</body>
</html>
```